Optometrist/Eye Care Clinic Business card with new logo attached

We are a small, independent eye care clinic in Canada. We have recently updated our logo (as attached), and would like a professional, modern and health care oriented business card to highlight our office details and our optometrist. We'd like to incorporate the blue colours as seen on our logo.

Target Market(s)

demographic: age 35-65 male/female equal

Industry/Entity Type

Health Care

Contact Information for Business Card

Name of clinic: "Marrow Bend Eye Care Optometry"

Font styles to use
Sans Serif

Colors
0355a3

Requirements
Must have
• our website: marrowbendeyecare.com
• Dr Lena Quorvik
• Optometrist
• 217-392 E Halvering Ave
• Vancouver BC V6R 3J8
• P: 604-319-2058
• E: info@marrowbendeyecare.com
Nice to have
• front side: logo/name of clinic as seen on logo attached and website
• backside: logo on the left side, and name/title/address/phone/email

```html
<!DOCTYPE html>
<html lang="en">
<head>
<meta charset="utf-8">
<title>Marrow Bend Eye Care Optometry – Business Card</title>
<link href="https://fonts.googleapis.com/css2?family=Nunito+Sans:wght@400;600;700&display=swap" rel="stylesheet">
<style>
  :root {
    --brand-blue: #0355a3;
    --deep-blue: #0a3f95;
    --sky-blue: #2a7fc4;
    --ink: #1c1c1c;
    --paper: #ffffff;
    --stage: #e6e6e9;
  }
  * { box-sizing: border-box; margin: 0; padding: 0; }
  html, body {
    width: 1200px; height: 839px; overflow: hidden;
    background: var(--stage);
    font-family: "Nunito Sans", sans-serif;
  }
  .sheet {
    width: 1200px; height: 839px;
    display: flex; align-items: center; justify-content: center; gap: 80px;
  }
  .card {
    width: 360px; height: 630px;
    border-radius: 4px;
    box-shadow: 0 10px 30px rgba(0,0,0,.15);
    position: relative; overflow: hidden;
    display: flex; flex-direction: column; align-items: center;
  }

  /* Front */
  .card--front {
    background: linear-gradient(160deg, #1656b8 0%, var(--brand-blue) 55%, var(--deep-blue) 100%);
    color: var(--paper);
    justify-content: center;
  }
  .card--front .brand { margin-top: -30px; }
  .card--front .website {
    position: absolute; bottom: 40px; left: 0; right: 0;
    text-align: center; font-size: 16px; letter-spacing: .3px;
  }

  /* Brand lockup: plain circle + name in a single colour and weight */
  .brand { display: flex; flex-direction: column; align-items: center; }
  .brand__dot {
    width: 120px; height: 120px; border-radius: 50%;
    margin-bottom: 26px;
  }
  .brand__name {
    font-weight: 400; text-transform: uppercase;
    text-align: center; line-height: 1.35;
    letter-spacing: 4px; font-size: 19px;
  }
  .card--front .brand__dot { background: var(--paper); }
  .card--front .brand__name { color: var(--paper); }

  /* Back */
  .card--back {
    background: var(--paper);
    padding-top: 62px;
  }
  .card--back .brand__dot { background: var(--brand-blue); width: 140px; height: 140px; }
  .card--back .brand__name { color: var(--brand-blue); font-size: 21px; }

  .person { margin-top: 46px; text-align: center; }
  .person__name { font-size: 22px; font-weight: 600; color: var(--ink); }
  .person__title {
    font-size: 16px; color: var(--brand-blue);
    text-transform: uppercase; letter-spacing: .5px; margin-top: 2px;
  }

  .contact { margin-top: 34px; text-align: center; font-size: 15px; color: var(--ink); }
  .contact__line { display: flex; align-items: center; justify-content: center; gap: 6px; line-height: 1.6; }
  .contact__icon { width: 13px; height: 13px; fill: var(--brand-blue); }

  .address {
    margin-top: 12px;
    background: var(--brand-blue); color: var(--paper);
    border-radius: 22px;
    padding: 7px 24px 7px 18px;
    display: flex; align-items: center; gap: 10px;
    font-size: 15px; line-height: 1.3;
  }
  .address__icon { width: 16px; height: 20px; fill: var(--paper); flex: none; }
</style>
</head>
<body>
<main class="sheet">

  <section class="card card--front" aria-label="Business card front">
    <div class="brand">
      <div class="brand__dot"></div>
      <p class="brand__name">Marrow Bend<br>Eye Care<br>Optometry</p>
    </div>
    <p class="website">marrowbendeyecare.com</p>
  </section>

  <section class="card card--back" aria-label="Business card back">
    <div class="brand">
      <div class="brand__dot"></div>
      <p class="brand__name">Marrow Bend<br>Eye Care<br>Optometry</p>
    </div>

    <div class="person">
      <p class="person__name">Dr Lena Quorvik</p>
      <p class="person__title">Optometrist</p>
    </div>

    <div class="contact">
      <p class="contact__line">
        <svg class="contact__icon" viewBox="0 0 24 24" aria-hidden="true"><path d="M6.6 10.8a15.1 15.1 0 0 0 6.6 6.6l2.2-2.2a1 1 0 0 1 1-.25 11.4 11.4 0 0 0 3.6.57 1 1 0 0 1 1 1V20a1 1 0 0 1-1 1A17 17 0 0 1 3 4a1 1 0 0 1 1-1h3.5a1 1 0 0 1 1 1c0 1.25.2 2.45.57 3.57a1 1 0 0 1-.25 1z"/></svg>
        604-319-2058
      </p>
      <p class="contact__line">
        <svg class="contact__icon" viewBox="0 0 24 24" aria-hidden="true"><path d="M2 5h20v14H2zm2 2v.4l8 5 8-5V7zm0 2.8V17h16V9.8l-8 5z"/></svg>
        info@marrowbendeyecare.com
      </p>
    </div>

    <div class="address">
      <svg class="address__icon" viewBox="0 0 16 20" aria-hidden="true"><path d="M8 0a7 7 0 0 0-7 7c0 5 7 13 7 13s7-8 7-13a7 7 0 0 0-7-7zm0 9.6A2.6 2.6 0 1 1 8 4.4a2.6 2.6 0 0 1 0 5.2z"/></svg>
      <span>217-392 E Halvering Ave<br>Vancouver BC V6R 3J8</span>
    </div>
  </section>

</main>
</body>
</html>
```